Tessellaria

Club flyer, grand opening night, house/electronic music, looking for clean design with a sample image attached. Please look at the prior flyers to get an idea of the style. Guaranteed project
I would like to use the red design if possible (tessellaria flyer attached)
Text:
TESSELLARIA
Winter House Music Monthly
Opening Night Dec 13 2013
Pellmont (use logo)
Featuring
BRAMOX (House/Garage)
(use logo with just Bramox name)
w/ resident
ORV (Driftwerk)
Free All Night
21-39 year old club with all house/electronic music. classier and grown up over gimmicky
Club

```html
<!DOCTYPE html>
<html lang="en">
<head>
<meta charset="utf-8">
<title>Tessellaria — Winter House Music Monthly</title>
<link rel="stylesheet" href="https://fonts.googleapis.com/css2?family=Montserrat:wght@300;400;700;800&family=Rubik+Dirt&family=Audiowide&display=swap">
<style>
  :root {
    --magenta: #e8196f;
    --magenta-deep: #d60f62;
    --blush: #f7a9c9;
    --paper: #ffffff;
  }
  * { margin: 0; padding: 0; box-sizing: border-box; }
  html, body { width: 1200px; height: 1200px; overflow: hidden; background: var(--paper); }
  .flyer {
    position: relative;
    width: 1200px;
    height: 1200px;
    overflow: hidden;
    background: var(--paper);
    font-family: "Montserrat", "Helvetica Neue", Arial, sans-serif;
    color: var(--magenta);
  }
  .burst {
    position: absolute;
    left: -600px;
    top: -10px;
    width: 1200px;
    height: 1200px;
    background: radial-gradient(circle at center,
      var(--magenta-deep) 0%,
      var(--magenta) 18%,
      rgba(236, 64, 135, 0.8) 32%,
      rgba(242, 120, 170, 0.55) 42%,
      rgba(247, 169, 201, 0.25) 48%,
      rgba(255, 255, 255, 0) 50%);
  }
  .venue-mark {
    position: absolute;
    left: 828px;
    top: 36px;
    width: 330px;
    height: 198px;
    display: flex;
    align-items: center;
    justify-content: center;
  }
  .venue-name {
    font-weight: 400;
    font-size: 42px;
    letter-spacing: 0.04em;
    color: var(--magenta);
  }
  .event-head {
    position: absolute;
    right: 42px;
    top: 288px;
    text-align: right;
  }
  .event-title {
    font-weight: 400;
    font-size: 46px;
    letter-spacing: 0.6em;
    margin-right: -0.6em;
    line-height: 1;
  }
  .event-tagline, .event-date {
    font-weight: 300;
    font-size: 34px;
    line-height: 1.2;
    letter-spacing: -0.01em;
  }
  .event-tagline { margin-top: 20px; }
  .event-date { margin-top: 12px; }
  .lineup {
    position: absolute;
    right: 62px;
    top: 762px;
    text-align: right;
  }
  .lineup-intro {
    font-weight: 300;
    font-size: 42px;
    line-height: 1.1;
  }
  .act { line-height: 1; white-space: nowrap; }
  .act-headliner { margin-top: 14px; }
  .headliner-name {
    font-family: "Rubik Dirt", "Impact", sans-serif;
    font-size: 70px;
    letter-spacing: 0.02em;
  }
  .resident-intro {
    font-weight: 300;
    font-size: 32px;
    line-height: 1;
    margin-top: 20px;
  }
  .act-resident { margin-top: 10px; }
  .act-name { font-weight: 800; font-size: 64px; letter-spacing: -0.01em; }
  .act-note { font-weight: 700; font-size: 32px; margin-left: 8px; }
  .act-note-crew { font-family: "Audiowide", "Arial", sans-serif; font-weight: 400; font-size: 30px; }
  .admission {
    position: absolute;
    right: 62px;
    top: 1108px;
    font-weight: 400;
    font-size: 32px;
  }
</style>
</head>
<body>
<main class="flyer">
  <div class="burst" role="img" aria-label="Pink kaleidoscopic radial burst illustration spreading from the left edge"></div>

  <div class="venue-mark">
    <span class="venue-name">PELLMONT</span>
  </div>

  <header class="event-head">
    <h1 class="event-title">TESSELLARIA</h1>
    <p class="event-tagline">Winter House Music Monthly</p>
    <p class="event-date">Opening Night Dec 13 2013</p>
  </header>

  <section class="lineup">
    <p class="lineup-intro">Featuring</p>
    <p class="act act-headliner"><span class="headliner-name">BRAMOX</span><span class="act-note">(House/Garage)</span></p>
    <p class="resident-intro">w/ resident</p>
    <p class="act act-resident"><span class="act-name">ORV</span><span class="act-note act-note-crew">(DRIFTWERK)</span></p>
  </section>

  <p class="admission">Free All Night</p>
</main>
</body>
</html>
```